Bicycle tour magazine

Actually, it's not a magazine. But I'd like it to look like one.

We have a bicycle tour. People who do these bicycle tours are given a 10-12 page packet outlining the day-to-day itinerary and explaining what they will see. We've been using the same (boring) Word template for 5 years now and need to update this to look more professional.

We have three different tours, but this first project is for one tour (basically the information on the attached PDF)

The magazine will have these different sections:
a. Why this tour
b. Preparing for this tour (which will contain: short texts on "What to pack", "How to train", etc.
c. Day 1, 2, 3, 4, 5, 6, 7, 8, 9, 10
Each of the above "Days" will have very short "articles" like:
"The numbers"
(the kilometers ridden, the meters climbed, etc)

"The Route"
Navigation directions...be careful turning here, etc.

"Points of Interest"
What they will be seeing today

"Where to Eat",
Suggestions on where to eat

"The Hotel"
A bit of information about the hotel

Target Market(s)

English speaking cyclists...UPSCALE.

Industry/Entity Type

Tour

Font styles to use
Sans Serif

Colors
f04a50

Requirements
Must have
• 1. take the information on the PDF update the layout using a more advanced template (illustrator ? photoshop ?)
• 2. New PDF should come in three versions:
• a. version suitable for computer viewing
• b. version suitable for laser printer
• c. version suitable for press printing (if we decide to go that route)
• 3. New design should look like a magazine page, with headers, etc. Pleases include attached map and add your own generic pictures (two or three ) as I would like to have pictures of scenery shown on these pages.
• 4. The attached pdf includes the information that has been present until now. However, since we're making this information look like a magazine, I imagine that we'll be using space much differently....making it feel lighter, less dense. etc.
• Please google "Pedalmorvent" to see company website.
• Photos at: https://www.snapvault.example/photos/pedalmorvent/collections/48302916573410298/
Nice to have
• Ideally, the person doing this project will also have experience with ibook and kindle OS, as we would eventually like these PDFs to have an electronic book format and made available on these platforms.
• Here are some templates I like:
• http://layoutbazaar.example/item/minimal-magazine-3/5183047?WT.oss_phrase=&WT.oss_rank=33&WT.z_author=TallHerons&WT.ac=search_thumb
• http://layoutbazaar.example/item/indesign-magazine-template/4829305?WT.oss_phrase=&WT.oss_rank=207&WT.z_author=katrubel&WT.ac=search_thumb
• http://layoutbazaar.example/item/elegant-art-magazine-template/537062?
• WT.oss_phrase=Magazine%20template&WT.oss_rank=22&WT.z_author=craftedVolmark&WT.ac=search_thumb

```html
<!DOCTYPE html>
<html lang="en">
<head>
<meta charset="utf-8">
<title>Pedalmorvent Tour Booklet – Spreads</title>
<link href="https://fonts.googleapis.com/css2?family=Oswald:wght@500;700&family=PT+Sans:wght@400;700&display=swap" rel="stylesheet">
<style>
  :root{
    --red:#e42530;
    --blue:#3f87c7;
    --navy:#163352;
    --ink:#0f2136;
    --white:#ffffff;
    --black:#111111;
    --stage:#ebe8e3;
    --sky:#8fb7d8;
    --meadow:#6f8f5a;
  }
  *{box-sizing:border-box;margin:0;padding:0}
  html,body{width:1200px;height:759px;overflow:hidden}
  body{background:var(--stage);font-family:"PT Sans",Arial,sans-serif;color:var(--ink);position:relative}

  .booklet{position:absolute;left:100px;top:115px;display:grid;
    grid-template-columns:repeat(6,134px);grid-template-rows:repeat(2,225px);
    column-gap:9px;row-gap:4px}

  .page{position:relative;background:var(--blue);overflow:hidden;
    box-shadow:0 2px 5px rgba(0,0,0,.25)}

  .masthead{height:30px;background:var(--red);display:flex;align-items:center;
    justify-content:center;gap:4px;border-bottom:2px solid var(--white)}
  .brand-dot{width:9px;height:9px;border-radius:50%;background:var(--white)}
  .brand{font-family:"Oswald",Arial,sans-serif;font-weight:700;font-size:12px;
    letter-spacing:.5px;text-transform:uppercase;color:var(--white)}

  /* Day card with facts table */
  .day-card{margin:5px 6px 3px;background:var(--white);display:grid;
    grid-template-columns:58px 1fr;min-height:44px}
  .day-title{padding:3px 3px 2px}
  .route-kind{font-family:"Oswald",Arial,sans-serif;font-weight:500;font-size:4.5px;line-height:6px;color:var(--ink)}
  .route-name{font-family:"Oswald",Arial,sans-serif;font-weight:700;font-size:7.5px;line-height:8px;color:var(--ink)}
  .route-name small{display:block;font-size:4.6px;line-height:5.6px;font-weight:500}
  .day-tag{font-family:"Oswald",Arial,sans-serif;font-weight:700;font-size:13px;line-height:14px;color:var(--red)}
  .route-facts{border-left:1px solid var(--red);font-size:3.4px;line-height:5.6px}
  .route-facts dt{display:inline;color:var(--red);font-weight:700}
  .route-facts dd{display:inline;color:var(--ink)}
  .route-facts div{padding:0 2px;border-bottom:.5px solid #cfd6de;white-space:nowrap;overflow:hidden}
  .route-facts div:first-child{background:var(--red)}
  .route-facts div:first-child dt,.route-facts div:first-child dd{color:var(--white)}

  .poi{margin:0 6px 3px;background:var(--white);padding:1px 3px 2px}
  .poi-title{font-family:"Oswald",Arial,sans-serif;font-weight:700;font-size:4.6px;line-height:6px;color:var(--ink)}
  .poi li{list-style:none;font-size:3.5px;line-height:4.6px;color:var(--red);font-weight:700}

  /* Day banner */
  .day-banner{margin:5px 6px 3px;background:var(--white)}
  .banner-top{display:flex;align-items:center;justify-content:space-between;padding:2px 3px}
  .banner-kind{font-family:"Oswald",Arial,sans-serif;font-weight:700;font-size:8px;color:var(--black);text-transform:uppercase}
  .banner-day{font-family:"Oswald",Arial,sans-serif;font-weight:700;
    font-size:12px;line-height:12px;color:var(--red);text-align:right}
  .banner-day small{display:block;font-size:4px;line-height:5px;color:var(--ink)}
  .route-bar{background:var(--black);color:var(--red);font-family:"Oswald",Arial,sans-serif;
    font-weight:700;font-size:6px;line-height:7px;padding:1.5px 3px;text-transform:uppercase}
  .route-bar.light{color:var(--white)}

  .article-body{padding:2px 7px 0;font-size:3.9px;line-height:5px;color:var(--ink);
    max-height:150px;overflow:hidden}
  .article-body p{margin-bottom:2.6px}
  .timetable{list-style:none;display:grid;grid-template-columns:1fr 1fr;gap:0 6px;
    font-size:3.6px;line-height:4.6px;margin-bottom:4px}

  .page-mark{position:absolute;left:50%;bottom:6px;width:9px;height:9px;margin-left:-4.5px;
    background:var(--red);border:1px solid var(--white)}

  /* Cover */
  .cover{background:var(--navy)}
  .cover .masthead{height:36px;margin:6px 6px 0;border-bottom:none}
  .cover .brand{font-size:13px}
  .cover-photo{position:absolute;left:6px;right:6px;top:48px;height:118px;
    background:linear-gradient(180deg,var(--sky) 0%,#b9cfe0 35%,#8ea07c 60%,var(--meadow) 100%)}
  .cover-emblem{position:absolute;left:50%;bottom:14px;width:30px;height:30px;margin-left:-15px;
    border-radius:50%;background:var(--red);border:2px solid var(--white)}
</style>
</head>
<body>
<main class="booklet">

  <!-- Row 1 -->
  <article class="page cover">
    <header class="masthead"><span class="brand-dot"></span><span class="brand">Pedalmorvent</span></header>
    <div class="cover-photo" role="img" aria-label="Group of cyclists posing on an alpine road with mountains behind"></div>
    <span class="cover-emblem"></span>
  </article>

  <article class="page">
    <header class="masthead"><span class="brand-dot"></span><span class="brand">Pedalmorvent</span></header>
    <section class="day-card">
      <div class="day-title">
        <p class="route-kind">Challenge Route</p>
        <h2 class="route-name">Geneve<small>to Chexbres</small></h2>
        <p class="day-tag">DAY 02</p>
      </div>
      <dl class="route-facts">
        <div><dt>To follow: </dt><dd>Route 2</dd></div>
        <div><dt>Map </dt><dd>Sheet 4</dd></div>
        <div><dt>GPS point </dt><dd>46.52 6.63</dd></div>
        <div><dt>Distance </dt><dd>78 km</dd></div>
        <div><dt>Watch out for </dt><dd>Tram rails</dd></div>
      </dl>
    </section>
    <section class="poi">
      <h3 class="poi-title">Point of interest</h3>
      <ul>
        <li>POI Old town and cathedral towers</li>
        <li>POI Lakeside castle and harbour</li>
        <li>POI Terraced vineyards above the lake</li>
      </ul>
    </section>
    <div class="article-body">
      <p>Start the morning on the lakeside path and keep the water on your right until the first village. Traffic is light before nine, so leave early and enjoy the quiet shore.</p>
      <p>Beyond the harbour the path joins a quiet road through small towns. Follow the red route signs and stay alert at the roundabouts, where drivers rarely expect riders.</p>
      <p>Climb gently through the vineyards above the lake. The road narrows near the church, so ride single file and watch for tractors coming down from the terraces.</p>
      <p>Lunch is best taken in the old market square, where several cafes serve fresh fish from the lake and simple salads at shaded tables.</p>
      <p>The last climb to the hotel is short but steep. Choose an easy gear early, stay seated and take your time. The view from the top is worth every turn of the pedals.</p>
      <p>Dinner is served on the terrace at seven. Bikes are kept in the locked room beside the reception.</p>
    </div>
    <span class="page-mark"></span>
  </article>

  <article class="page">
    <header class="masthead"><span class="brand-dot"></span><span class="brand">Pedalmorvent</span></header>
    <section class="day-banner">
      <div class="banner-top">
        <h2 class="banner-kind">Challenge Route</h2>
        <p class="banner-day">DAY 02<small>Page 2</small></p>
      </div>
      <p class="route-bar">Geneva → Chexbres</p>
    </section>
    <div class="article-body">
      <p>Past the old harbour the route turns inland. Follow the signs for the cycle path and stay on the left bank of the river until you reach the wooden bridge.</p>
      <p>Water is available at the fountain in the square. The cafe beside it serves excellent tarts and coffee, and the staff are used to hungry riders arriving mid morning.</p>
      <p>After the bridge the road rises through farmland for about six kilometres. The gradient is steady and the surface smooth, so settle into a rhythm and enjoy the open fields.</p>
      <p>At the top of the rise turn right toward the lake. The descent is fast with two sharp bends near the bottom. Brake before each bend, not inside it, and keep your weight back.</p>
      <p>The lakeside town below has a fine museum and a chocolate shop that most riders find hard to pass. Allow half an hour if you plan to stop here.</p>
      <p>From the town the route follows the shore once more before the final climb into the vines. Take plenty of water for this section, as there is little shade after noon.</p>
      <p>Evening walks through the vineyard paths are highly recommended.</p>
    </div>
    <span class="page-mark"></span>
  </article>

  <article class="page">
    <header class="masthead"><span class="brand-dot"></span><span class="brand">Pedalmorvent</span></header>
    <section class="day-card">
      <div class="day-title">
        <p class="route-kind">Challenge Route</p>
        <h2 class="route-name">Chexbres<small>to Saanen-Gstaad</small></h2>
        <p class="day-tag">DAY 03</p>
      </div>
      <dl class="route-facts">
        <div><dt>To follow: </dt><dd>Route 3</dd></div>
        <div><dt>Map </dt><dd>Sheet 5</dd></div>
        <div><dt>GPS point </dt><dd>46.47 7.28</dd></div>
        <div><dt>Distance </dt><dd>84 km</dd></div>
        <div><dt>Watch out for </dt><dd>Loose gravel</dd></div>
      </dl>
    </section>
    <section class="poi">
      <h3 class="poi-title">Point of interest</h3>
      <ul><li>POI Gruyères castle and cheese dairy</li></ul>
    </section>
    <div class="article-body">
      <p>Today climbs into the hills above the lake. Take the long descent slowly, as the surface is rough in places and the bends tighten near the bottom of the valley.</p>
      <p>The cheese dairy in the valley opens at ten. Stop for a tasting and a look at the copper vats before heading on to the hilltop town and its small castle.</p>
      <p>The castle courtyard is free to enter and the ramparts give a wide view over the valley. Leave your bikes at the rack by the gate and walk up the cobbled street.</p>
      <p>After lunch the route follows the river upstream. The road is quiet but has a short gravel section near the dam, so ride carefully and keep a loose grip on the bars.</p>
      <p>The final part climbs gently into the chalet country. Farm shops along the road sell cold drinks and fruit, a welcome break on a warm afternoon.</p>
      <p>Arrive at the hotel before six to enjoy the spa, which is included for all riders this evening.</p>
    </div>
    <span class="page-mark"></span>
  </article>

  <article class="page">
    <header class="masthead"><span class="brand-dot"></span><span class="brand">Pedalmorvent</span></header>
    <section class="day-card">
      <div class="day-title">
        <p class="route-kind">Challenge Route</p>
        <h2 class="route-name">Saanen-Gstaad<small>to Interlaken Wengen</small></h2>
        <p class="day-tag">DAY 04</p>
      </div>
      <dl class="route-facts">
        <div><dt>To follow: </dt><dd>Route 4</dd></div>
        <div><dt>Map </dt><dd>Sheet 6</dd></div>
        <div><dt>GPS point </dt><dd>46.60 7.91</dd></div>
        <div><dt>Distance </dt><dd>92 km</dd></div>
        <div><dt>Watch out for </dt><dd>Dark tunnels</dd></div>
      </dl>
    </section>
    <div class="article-body">
      <p>Leave the chalet town on the valley road and cross the pass before noon. The summit restaurant has a terrace with a wide view of the glaciers and the peaks beyond.</p>
      <p>The climb is long but never steep. Most riders take about ninety minutes from the valley floor. Wear a light layer for the top, where the wind can be cool even in summer.</p>
      <p>The descent to the lakes is long and fast. Keep your speed down in the tunnels and switch on your lights before you enter each one. Traffic is heavier here at weekends.</p>
      <p>At the lake follow the signed cycle path along the northern shore. It runs through orchards and small harbours and is almost completely flat.</p>
      <p>In town, load your bike onto the mountain train for the last part of the journey. Tickets are included and the staff will help you with the bike racks.</p>
      <p>Your hotel sits at the foot of the great north face. Ask for a room with a balcony and watch the evening light on the snow.</p>
      <p>Dinner tonight features local lamb and garden vegetables.</p>
    </div>
    <span class="page-mark"></span>
  </article>

  <article class="page">
    <header class="masthead"><span class="brand-dot"></span><span class="brand">Pedalmorvent</span></header>
    <section class="day-banner">
      <div class="banner-top">
        <h2 class="banner-kind">Challenge Route</h2>
        <p class="banner-day">DAY 05</p>
      </div>
      <p class="route-bar light">Wengen Hike</p>
    </section>
    <div class="article-body">
      <p>A rest day for the legs. Take the cog railway up the mountain and walk the high trail back down through meadows, farms and quiet pine forest.</p>
      <p>Bring a warm layer and a rain jacket, as the weather changes quickly at altitude. The trail is well marked and takes about four hours at an easy pace.</p>
      <p>Halfway down, a small mountain hut serves soup, rösti and fresh milk. It is the perfect place for lunch, with a view straight across to the glaciers.</p>
      <p>If you prefer a shorter day, take the cable car down from the hut and spend the afternoon in the village, where the shops and cafes line the main street.</p>
      <p>For those who want more, a longer loop continues to the waterfall valley. Ask at reception for a map and the latest trail conditions before setting off.</p>
      <p>The hotel will prepare a packed lunch if you order it the evening before.</p>
    </div>
    <span class="page-mark"></span>
  </article>

  <!-- Row 2 -->
  <article class="page">
    <header class="masthead"><span class="brand-dot"></span><span class="brand">Pedalmorvent</span></header>
    <section class="day-card">
      <div class="day-title">
        <p class="route-kind">Challenge Route</p>
        <h2 class="route-name">Interlaken<small>Wengen to Lucerne</small></h2>
        <p class="day-tag">DAY 06</p>
      </div>
      <dl class="route-facts">
        <div><dt>To follow: </dt><dd>Route 6</dd></div>
        <div><dt>Map </dt><dd>Sheet 7</dd></div>
        <div><dt>GPS point </dt><dd>47.05 8.31</dd></div>
        <div><dt>Distance </dt><dd>88 km</dd></div>
        <div><dt>Watch out for </dt><dd>Lake traffic</dd></div>
      </dl>
    </section>
    <div class="article-body">
      <p>Take the train back down to the valley, then ride along both lakes before turning north toward the hills. The road beside the first lake is flat and shaded.</p>
      <p>At the end of the second lake the route begins the climb to the pass. It is steady rather than steep, with a few hairpins near the top and good views back to the peaks.</p>
      <p>The pass has a small kiosk and a lake for a quick swim on hot days. Fill your bottles here, as the next water stop is twenty kilometres away.</p>
      <p>From the top it is downhill almost all the way to the city. The descent has fresh tarmac and long straight sections, so it is safe to let the bike run.</p>
      <p>In the city follow the blue lane along the river to the old town. Your hotel is close to the covered wooden bridge and the water tower.</p>
      <p>The evening is free. The lakeside promenade has many restaurants, and the boat trips at sunset are well worth the short wait.</p>
    </div>
    <span class="page-mark"></span>
  </article>

  <article class="page">
    <header class="masthead"><span class="brand-dot"></span><span class="brand">Pedalmorvent</span></header>
    <section class="day-card">
      <div class="day-title">
        <p class="route-kind">Challenge Route</p>
        <h2 class="route-name">Lucerne<small>to Rapperswil</small></h2>
        <p class="day-tag">DAY 07</p>
      </div>
      <dl class="route-facts">
        <div><dt>To follow: </dt><dd>Route 9</dd></div>
        <div><dt>Map </dt><dd>Sheet 8</dd></div>
        <div><dt>GPS point </dt><dd>47.22 8.81</dd></div>
        <div><dt>Distance </dt><dd>76 km</dd></div>
        <div><dt>Watch out for </dt><dd>City junctions</dd></div>
      </dl>
    </section>
    <section class="poi">
      <ul><li>POI Einsiedeln Abbey (2 km off route)</li></ul>
    </section>
    <div class="article-body">
      <p>Leave the city along the lake shore and follow the national route signs east. The morning section is gentle, with several good places to stop for coffee.</p>
      <p>The city junctions can be busy before nine. Stay in the cycle lane, use hand signals and wait for the green bike light at the larger crossings.</p>
      <p>After the second lake the road rises through orchards and small farms toward the abbey. The short detour is signed and the church interior is remarkable.</p>
      <p>Lunch options are limited after the abbey, so consider eating in the village square. The bakery opposite the church sells excellent pastries for the road.</p>
      <p>The afternoon brings a long, gentle descent to the lake. Arrive in the rose town by late afternoon and walk up to the castle gardens for sunset.</p>
      <p>The hotel faces the harbour and has a private garage for bikes.</p>
    </div>
    <span class="page-mark"></span>
  </article>

  <article class="page">
    <header class="masthead"><span class="brand-dot"></span><span class="brand">Pedalmorvent</span></header>
    <section class="day-card">
      <div class="day-title">
        <p class="route-kind">Challenge Route</p>
        <h2 class="route-name">Rapperswil<small>to Sax</small></h2>
        <p class="day-tag">DAY 08</p>
      </div>
      <dl class="route-facts">
        <div><dt>To follow: </dt><dd>Route 9</dd></div>
        <div><dt>Map </dt><dd>Sheet 9</dd></div>
        <div><dt>GPS point </dt><dd>47.23 9.45</dd></div>
        <div><dt>Distance </dt><dd>81 km</dd></div>
        <div><dt>Watch out for </dt><dd>Narrow bridge</dd></div>
      </dl>
    </section>
    <div class="article-body">
      <p>Cross the long wooden footbridge at the start of the day, walking your bike. Then follow the lake path before climbing into the green hills to the east.</p>
      <p>The first climb is the hardest of the day, about five kilometres with a few steep ramps. Take it slowly, as there is plenty of riding still to come.</p>
      <p>Beyond the ridge the route drops into a wide valley of farms and small lakes. The roads are quiet and the cows often outnumber the cars here.</p>
      <p>Watch for the narrow bridge over the river near the old mill. Give way to oncoming traffic and cross one rider at a time.</p>
      <p>The afternoon follows the broad river valley south, with the mountains of the small neighbouring country on your left and the cliffs on your right.</p>
      <p>The village inn serves a fine local menu. Ask for a table on the garden terrace and try the trout if it is on the board that evening.</p>
    </div>
    <span class="page-mark"></span>
  </article>

  <article class="page">
    <header class="masthead"><span class="brand-dot"></span><span class="brand">Pedalmorvent</span></header>
    <section class="day-card">
      <div class="day-title">
        <p class="route-kind">Challenge Route</p>
        <h2 class="route-name">Sax to<small>Arbon/Rorschach</small></h2>
        <p class="day-tag">DAY 09</p>
      </div>
      <dl class="route-facts">
        <div><dt>To follow: </dt><dd>Route 2</dd></div>
        <div><dt>Map </dt><dd>Sheet 10</dd></div>
        <div><dt>GPS point </dt><dd>47.51 9.43</dd></div>
        <div><dt>Distance </dt><dd>58 km</dd></div>
        <div><dt>Watch out for </dt><dd>Level crossing</dd></div>
      </dl>
    </section>
    <div class="article-body">
      <p>A short day with a long descent to the big lake. Follow the river valley north and keep to the cycle lane through the busier towns along the way.</p>
      <p>The dyke path beside the river is smooth and car free. It is often windy, so ride in a group and take turns at the front to share the work.</p>
      <p>Watch out for the level crossing near the station. The rails cross the road at an angle, so take them straight on and slowly, especially in the wet.</p>
      <p>At the river mouth a nature reserve offers a good stop. Herons and grebes nest in the reeds, and a wooden tower gives a fine view across the water.</p>
      <p>The final kilometres follow the lake shore past small beaches and boat harbours. Several lakeside kiosks sell ice cream and cold drinks.</p>
      <p>You will reach the hotel early, leaving the whole afternoon for a swim or a walk through the old town.</p>
    </div>
    <span class="page-mark"></span>
  </article>

  <article class="page">
    <header class="masthead"><span class="brand-dot"></span><span class="brand">Pedalmorvent</span></header>
    <section class="day-banner">
      <div class="banner-top">
        <h2 class="banner-kind">Challenge Route</h2>
        <p class="banner-day">DAY 09<small>Page 02</small></p>
      </div>
      <p class="route-bar light">Sax to Arbon/Rorschach</p>
    </section>
    <div class="article-body">
      <p>Spend the afternoon on the lake promenade or take the ferry across to the far shore for an evening walk through the harbour town and its painted houses.</p>
      <p>Ferries leave every hour from the pier beside the hotel. Bikes travel free, so you can also ride a short loop on the far side and return by the last boat.</p>
      <p>The old town has a fine abbey library, one of the oldest in Europe. Felt slippers are provided at the door to protect the wooden floors.</p>
      <p>For dinner, the fish restaurant on the pier is a favourite with our riders. Book a table through reception, as it fills quickly on summer evenings.</p>
      <p>The hotel sits right on the water. Bikes are stored in the locked garage behind the building, and breakfast starts at seven on the terrace.</p>
      <p>Tomorrow is the last day, so pack your bags tonight.</p>
    </div>
    <span class="page-mark"></span>
  </article>

  <article class="page">
    <header class="masthead"><span class="brand-dot"></span><span class="brand">Pedalmorvent</span></header>
    <section class="day-banner">
      <div class="banner-top">
        <h2 class="banner-kind">Challenge Route</h2>
        <p class="banner-day">DAY 10<small>Page 02</small></p>
      </div>
      <p class="route-bar">Return to Geneva via Berne</p>
      <p class="route-bar light">Return to Geneva through Berne on Train</p>
    </section>
    <div class="article-body">
      <p>Ride to the station after breakfast and load your bike onto the train. Our guide will meet you on the platform with tickets and reservations.</p>
      <ul class="timetable">
        <li>08:00 Breakfast</li>
        <li>09:15 Ride to station</li>
        <li>10:02 Train departs</li>
        <li>12:30 Lunch in the capital</li>
        <li>14:05 Train to the lake</li>
        <li>16:40 Arrive and farewell</li>
      </ul>
      <p>Change trains in the capital and allow time for a short walk through its arcaded old streets, the bear park and the rose garden above the river.</p>
      <p>The last train runs along the lake and through the vineyards you rode on the second day, a fine way to look back on the journey.</p>
      <p>Thank you for riding with us. We hope the roads, the views and the company stay with you long after the last climb.</p>
    </div>
    <span class="page-mark"></span>
  </article>

</main>
</body>
</html>
```